Yoga Shool offering Teacher Training in a new venue

I need to advertise our 200Hr Teacher Training course at the Fernhill Arena, I want to attract yoga students who want to be teachers as well as those looking to deepen their personal practice and attend for personal growth. I introduced yoga classes to this venue when it first opened in 2000, and I am returning with this Teacher Training course. My website colours are brown and orange.

Target Market(s)

Yoga Students around the venue

Font styles to use
Sans Serif

Colors

Designer to choose colors to be used in the design.

Requirements
Must have
• logo,

```html
<!DOCTYPE html>
<html lang="en">
<head>
<meta charset="utf-8">
<title>Yoga Cadence Teacher Training Flyer</title>
<link href="https://fonts.googleapis.com/css2?family=Oswald:wght@600;700&family=Montserrat:wght@400;500;700;800&display=swap" rel="stylesheet">
<style>
  :root {
    --brown: #5b3a3c;
    --orange: #ee7623;
    --white: #ffffff;
    --ink: #3a2a2b;
    --backdrop: #d4d4d4;
  }
  * { margin: 0; padding: 0; box-sizing: border-box; }
  html, body { width: 1200px; height: 1141px; overflow: hidden; }
  body { background: var(--backdrop); font-family: "Montserrat", sans-serif; color: var(--ink); }

  .flyer {
    position: absolute; left: 220px; top: 20px;
    width: 760px; height: 1100px;
    background: var(--white); overflow: hidden;
    box-shadow: 0 6px 24px rgba(0,0,0,.18);
  }
  .flyer-art { position: absolute; inset: 0; }

  .brand-mark {
    position: absolute; left: 622px; top: 240px;
    width: 112px; height: 112px; border-radius: 50%;
    background: var(--brown);
    display: flex; align-items: center; justify-content: center;
    text-align: center;
    font-family: "Montserrat", sans-serif; font-weight: 800;
    font-size: 17px; line-height: 1.1; color: var(--orange);
  }

  .headline {
    position: absolute; left: 40px; top: 232px; width: 350px;
    font-family: "Oswald", sans-serif; font-weight: 700;
    text-transform: uppercase; color: var(--brown);
    font-size: 36px; line-height: 1.05;
  }
  .headline .venue {
    display: inline-block; margin-top: 6px;
    background: var(--orange); color: var(--white);
    padding: 2px 10px;
  }
  .divider { position: absolute; left: 40px; top: 470px; width: 60px; height: 6px; background: var(--brown); }
  .for-you {
    position: absolute; left: 40px; top: 484px;
    font-family: "Oswald", sans-serif; font-weight: 700;
    font-size: 34px; color: var(--brown); text-transform: uppercase;
  }
  .intro {
    position: absolute; left: 40px; top: 548px; width: 320px;
    font-size: 13px; line-height: 1.5;
  }
  .intro p + p { margin-top: 8px; }

  .ready {
    position: absolute; left: 400px; top: 492px; width: 320px;
    text-align: center; color: var(--white);
  }
  .ready-title { font-weight: 800; font-size: 38px; line-height: 1.02; text-transform: uppercase; }
  .ready-sub { margin-top: 10px; font-weight: 500; font-size: 17px; line-height: 1.3; }
  .ready-year { margin-top: 6px; font-weight: 800; font-size: 28px; }

  .love-yoga {
    position: absolute; left: 540px; top: 688px;
    width: 120px; height: 120px; border-radius: 50%;
    background: var(--brown); color: var(--white);
    display: flex; align-items: center; justify-content: center; text-align: center;
    font-weight: 700; font-size: 17px; line-height: 1.1;
    border: 5px solid var(--white);
  }
  .question {
    position: absolute; left: 430px; top: 830px; width: 300px;
    text-align: center; font-weight: 500; font-size: 15px; line-height: 1.4;
  }

  .testimonials {
    position: absolute; left: 40px; top: 800px; width: 340px;
    font-size: 12px; line-height: 1.45;
  }
  .testimonials p + p { margin-top: 8px; }
  .testimonials cite { font-style: normal; font-weight: 700; }

  .footer-band {
    position: absolute; left: 0; bottom: 0; width: 760px; height: 70px;
    background: var(--brown); color: var(--white);
    display: flex; align-items: center; justify-content: center;
    font-size: 16px; font-weight: 500;
  }
  .footer-band .url { color: var(--orange); margin-left: 6px; }
</style>
</head>
<body>
  <article class="flyer">
    <svg class="flyer-art" width="760" height="1100" viewBox="0 0 760 1100">
      <defs>
        <linearGradient id="gardenTones" x1="0" y1="0" x2="0" y2="1">
          <stop offset="0" stop-color="#3f6a2e"/>
          <stop offset="0.55" stop-color="#8b8a78"/>
          <stop offset="1" stop-color="#4c5a34"/>
        </linearGradient>
        <linearGradient id="poseTones" x1="0" y1="0" x2="0" y2="1">
          <stop offset="0" stop-color="#7c9a5a"/>
          <stop offset="1" stop-color="#5a6e8a"/>
        </linearGradient>
      </defs>
      <polygon class="hero-photo" role="img" aria-label="Photo of a yoga teacher seated on a bench in a leafy garden"
               points="0,0 560,0 605,440 0,440" fill="url(#gardenTones)"/>
      <polygon class="peak peak-left" points="0,420 150,170 390,540 0,540" fill="var(--white)"/>
      <polygon class="peak peak-mid" points="380,540 470,330 560,540" fill="var(--white)"/>
      <circle class="ready-disc" cx="560" cy="560" r="190" fill="var(--orange)"/>
      <circle cx="470" cy="400" r="76" fill="var(--white)"/>
      <circle class="pose-photo" role="img" aria-label="Photo of a yoga student in warrior pose on a mat outdoors"
              cx="470" cy="400" r="68" fill="url(#poseTones)"/>
    </svg>

    <div class="brand-mark">Yoga<br>Cadence</div>

    <h1 class="headline">Yoga Cadence<br>Teacher Training<br>is coming to<br><span class="venue">The Fernhill Arena</span></h1>
    <div class="divider"></div>
    <h2 class="for-you">This is for you!</h2>
    <div class="intro">
      <p>Yoga Cadence Teacher Training isn't just for aspiring teachers, it's for any dedicated student of yoga to build a powerful personal practice and deepen their understanding and experience of yoga.</p>
      <p>Take the next step in your yoga and in your life, access new possibilities, check out what past trainees had to say.</p>
    </div>

    <div class="ready">
      <div class="ready-title">Are you<br>ready?</div>
      <div class="ready-sub">to set in motion a stunning<br>transformation in</div>
      <div class="ready-year">2019</div>
    </div>

    <div class="love-yoga">Do you<br>love<br>Yoga?</div>
    <p class="question">Do you want to know yourself, love yourself, heal yourself and treat yourself better?</p>

    <div class="testimonials">
      <p>"Wow! This course has been life changing in every way, it has given me so much confidence to do things I haven't done before." <cite>Sam Ellery 2018</cite></p>
      <p>"I love how we apply everything to our own lives – it's real and tangible, so we live it and learn it." <cite>Rory Dunmore 2016</cite></p>
      <p>"I loved every lesson, and as I applied the teachings to my life, they had a flow on effect to my family too. Prepare to not only become a yoga teacher, prepare to change in incredibly positive ways." <cite>Kathy Linden 2018</cite></p>
    </div>

    <footer class="footer-band">Course Details are available on our website <span class="url">www.yogacadence.example</span></footer>
  </article>
</body>
</html>
```